Our business deals with residential and commercial property management. We have commercial tenants willing to offer deals to our residential tenants. We want a very nice looking card stock where I can add (later) each specific deal/incentive. The template attached has two options but feel free to come up with what you think looks best. We need or logo and possibly this simple phrase as the title,

"Welcome to the Brelford Community!" OR "Join the Brelford Community"

This is optional, use discretion on what is should say:

"Every member of Brelford Commercial is important to us, be a part of our community and explore your neighborhood."

www.brelfordcommercial.example can give you a feel for our look and image. I was thinking of maybe a red & black color scheme.

***Each slot for the deal should be blank so I can add and change each deal later. These are going to be cut out so maybe the "-----" lines around the deals would look good. Thanks!!

Target Market(s)

Residential Tenants: Single & Multi Families

Industry/Entity Type

Property Management

Font styles to use
Serif

Colors
ec1f27
000000
fbfbfb

Requirements
Must have
• -Logo (Attached)
• -6 blank slots to add deals later (Can have more deals based on appropriate look)
• -either "Welcome to the Brelford Community" or "Join the Brelford Community"
• -Our phone number: 801.555.0147
• -Website: www.brelfordcommercial.example
• -Address: 417 E. Dunmore Way Suite 5, Centerville, UT 84099
Nice to have
• "Every member of Brelford Commercial is important to us, be a part of our community and explore your neighborhood."
• This could be something else that's similar but sounds better.
• Possible color options: red, black, white OR Your discretion.
Should not have
• Pictures of properties or people.

```html
<!DOCTYPE html>
<html lang="en">
<head>
<meta charset="utf-8">
<title>Welcome to the Brelford Community</title>
<link href="https://fonts.googleapis.com/css2?family=Playfair+Display:wght@400;700;900&family=Montserrat:wght@400;600;800&display=swap" rel="stylesheet">
<style>
  :root {
    --red: #ec1f27;
    --black: #000000;
    --off-white: #fbfbfb;
    --band: #1b1b1b;
    --ink: #222222;
    --badge: #b9b3ad;
  }
  * { box-sizing: border-box; margin: 0; padding: 0; }
  html, body { width: 900px; height: 1200px; overflow: hidden; background: var(--off-white); }
  .flyer { position: relative; width: 900px; height: 1200px; background: var(--off-white); font-family: 'Montserrat', sans-serif; color: var(--ink); }

  .hero { position: relative; width: 900px; height: 540px; }
  .hero svg { position: absolute; inset: 0; }
  .brand { position: absolute; right: 28px; top: 46px; text-align: right; color: var(--red); font-family: 'Montserrat', sans-serif; font-weight: 800; line-height: 1; }
  .brand .brand-name { display: block; font-size: 42px; letter-spacing: 1px; }
  .brand .brand-sub { display: block; font-size: 24px; letter-spacing: 2px; margin-top: 4px; }
  .headline { position: absolute; right: 28px; top: 378px; text-align: right; color: var(--off-white); font-family: 'Playfair Display', serif; text-transform: uppercase; line-height: 1.08; }
  .headline .lead { display: block; font-size: 38px; font-weight: 400; }
  .headline .main { display: block; font-size: 46px; font-weight: 900; }

  .mission { height: 84px; background: var(--band); color: var(--off-white); text-align: center; padding-top: 14px; text-transform: uppercase; }
  .mission .line-one { font-family: 'Playfair Display', serif; font-size: 25px; letter-spacing: .5px; }
  .mission .line-two { font-family: 'Montserrat', sans-serif; font-weight: 800; font-size: 16px; margin-top: 4px; letter-spacing: .5px; }

  .deals { padding: 22px 60px 0; }
  .deals-title { display: block; width: 290px; margin: 0 auto; border: 2px solid var(--red); color: var(--red); text-align: center; font-weight: 800; font-size: 20px; padding: 8px 0; }
  .deal-list { display: grid; grid-template-columns: 1fr 1fr; column-gap: 60px; row-gap: 14px; list-style: none; margin-top: 22px; font-size: 15px; line-height: 1.3; }
  .deal-list .partner { color: var(--red); font-weight: 800; text-transform: uppercase; }

  .partner-badges { display: flex; justify-content: center; gap: 74px; margin-top: 20px; }
  .badge { width: 40px; height: 24px; background: var(--badge); border-radius: 3px; }
  .badge.round { border-radius: 50%; width: 28px; height: 28px; }

  .slot-panel { position: absolute; left: 120px; top: 894px; width: 660px; height: 222px; background: var(--red); border-radius: 18px; padding: 18px 24px; display: grid; grid-template-columns: repeat(3, 1fr); grid-template-rows: 1fr 1fr; gap: 16px 24px; }
  .deal-slot { background: var(--off-white); border: 2px dashed var(--ink); }

  .contact-bar { position: absolute; left: 0; bottom: 0; width: 900px; height: 64px; background: var(--black); color: var(--off-white); padding: 10px 40px 0; font-size: 12px; }
  .contact-row { display: flex; justify-content: space-between; align-items: center; }
  .contact-item { display: flex; align-items: center; gap: 8px; }
  .contact-item svg { width: 14px; height: 14px; }
  .contact-address { justify-content: center; margin-top: 8px; }
</style>
</head>
<body>
<main class="flyer">
  <header class="hero">
    <svg width="900" height="540" viewBox="0 0 900 540">
      <defs>
        <linearGradient id="roomTones" x1="0" y1="0" x2="1" y2="1">
          <stop offset="0" stop-color="#8a827b"/>
          <stop offset=".45" stop-color="#e6e3df"/>
          <stop offset="1" stop-color="#5e5650"/>
        </linearGradient>
      </defs>
      <rect class="hero-photo" role="img" aria-label="Photo of a bright bedroom with a lamp and white pillows" width="900" height="540" fill="url(#roomTones)"/>
      <polygon class="hero-white" points="480,0 900,0 900,300" fill="#fbfbfb"/>
      <polygon class="hero-red" points="400,0 480,0 900,300 900,370" fill="#ec1f27"/>
      <polygon class="hero-black" points="470,360 900,360 900,540 330,540" fill="#000000"/>
      <polygon class="hero-red-edge" points="470,360 510,360 370,540 330,540" fill="#ec1f27"/>
    </svg>
    <div class="brand">
      <span class="brand-name">BRELFORD</span>
      <span class="brand-sub">COMMERCIAL</span>
    </div>
    <h1 class="headline">
      <span class="lead">Welcome to</span>
      <span class="main">The Brelford</span>
      <span class="main">Community!</span>
    </h1>
  </header>

  <section class="mission">
    <p class="line-one">Every member of Brelford Commercial is important to us</p>
    <p class="line-two">Be a part of our community and explore your neighborhood</p>
  </section>

  <section class="deals">
    <h2 class="deals-title">DEALS TO IMPLEMENT</h2>
    <ul class="deal-list">
      <li><span class="partner">Brelford:</span> Refer a friend to rent with us and both of you will receive $200 off rent.</li>
      <li><span class="partner">Summit Lending:</span> Free approval for a mortgage loan</li>
      <li><span class="partner">Maple Row:</span> Free designer earrings for you and a friend when you purchase $25+</li>
      <li><span class="partner">Brookside Dental:</span> Free Whitening</li>
      <li><span class="partner">Orbit Creamery:</span> BOGO Waffle Cone</li>
      <li><span class="partner">Nonna's:</span> 2 Fors $8</li>
    </ul>
    <div class="partner-badges">
      <span class="badge"></span>
      <span class="badge round"></span>
      <span class="badge"></span>
      <span class="badge"></span>
      <span class="badge round"></span>
      <span class="badge"></span>
    </div>
  </section>

  <section class="slot-panel" aria-label="Blank deal slots">
    <div class="deal-slot"></div>
    <div class="deal-slot"></div>
    <div class="deal-slot"></div>
    <div class="deal-slot"></div>
    <div class="deal-slot"></div>
    <div class="deal-slot"></div>
  </section>

  <footer class="contact-bar">
    <div class="contact-row">
      <span class="contact-item">
        <svg viewBox="0 0 24 24"><path fill="#fbfbfb" d="M6.6 10.8a15 15 0 0 0 6.6 6.6l2.2-2.2c.3-.3.7-.4 1-.2 1.1.4 2.3.6 3.6.6.6 0 1 .4 1 1V20c0 .6-.4 1-1 1A17 17 0 0 1 3 4c0-.6.4-1 1-1h3.5c.6 0 1 .4 1 1 0 1.3.2 2.5.6 3.6.1.3 0 .7-.2 1z"/></svg>
        801.555.0147
      </span>
      <span class="contact-item">
        <svg viewBox="0 0 24 24"><rect x="2" y="5" width="20" height="14" rx="2" fill="none" stroke="#fbfbfb" stroke-width="2"/><path d="M3 6l9 7 9-7" fill="none" stroke="#fbfbfb" stroke-width="2"/></svg>
        support@brelfordcommercial.example
      </span>
      <span class="contact-item">
        <svg viewBox="0 0 24 24"><circle cx="12" cy="12" r="9" fill="none" stroke="#fbfbfb" stroke-width="2"/><path d="M3 12h18M12 3c3 3 3 15 0 18M12 3c-3 3-3 15 0 18" fill="none" stroke="#fbfbfb" stroke-width="1.5"/></svg>
        www.brelfordcommercial.example
      </span>
    </div>
    <div class="contact-row contact-address">
      <span class="contact-item">
        <svg viewBox="0 0 24 24"><path fill="#fbfbfb" d="M12 2a7 7 0 0 0-7 7c0 5 7 13 7 13s7-8 7-13a7 7 0 0 0-7-7zm0 9.5A2.5 2.5 0 1 1 12 6.5a2.5 2.5 0 0 1 0 5z"/></svg>
        417 E. Dunmore Way Suite 5, Centerville, UT 84099
      </span>
    </div>
  </footer>
</main>
</body>
</html>
```